Info graphics

We have four infographics that we want recreated. We want the same information displayed but original artwork

Requirements
Must have
• We require a re-creation of each of the 4 infographics attached.

```html
<!DOCTYPE html>
<html lang="en">
<head>
<meta charset="utf-8">
<title>4G and 5G Infographics</title>
<link href="https://fonts.googleapis.com/css2?family=Montserrat:wght@200;300;600;700;900&family=Open+Sans:wght@400;600&display=swap" rel="stylesheet">
<style>
  :root{
    --red:#e31e24;
    --red-soft:#f36b6f;
    --ink:#231f20;
    --bar-dark:#333333;
    --panel:#eeeeee;
    --rule:#9fd8ea;
    --white:#ffffff;
    --muted:#6d6e71;
  }
  *{margin:0;padding:0;box-sizing:border-box}
  html,body{width:1200px;height:3025px;overflow:hidden;background:var(--white)}
  body{position:relative;font-family:"Open Sans",sans-serif;color:var(--ink)}
  .abs{position:absolute}
  .rule{position:absolute;height:1px;background:var(--rule)}
  .art{position:absolute;border-radius:6px}
  .art--city{background:linear-gradient(160deg,#dfe3e6 0%,#b9c0c4 60%,#5b9a55 100%)}
  .art--beam{background:linear-gradient(160deg,#dfe3e6 0%,#e8a3a5 55%,#5b9a55 100%)}
  .art--cone{background:linear-gradient(180deg,#f2f2f2 0%,#bdbdbd 100%)}
  .art--beams{background:linear-gradient(180deg,#f4f4f4 0%,#f5b3b5 100%)}

  .pill{position:absolute;border-radius:16px;color:var(--white);font-family:"Montserrat",sans-serif;font-weight:700;font-size:22px;line-height:22px;text-align:center;padding-top:15px}
  .pill--dark{background:#000}
  .pill--red{background:var(--red)}
  .callout{position:absolute;background:#000;color:var(--white);border-radius:18px;font-size:9px;line-height:11px;text-align:center;padding-top:7px}

  .section-title{position:absolute;left:0;width:1200px;text-align:center;font-family:"Montserrat",sans-serif;font-size:34px;letter-spacing:1px;color:var(--ink)}
  .section-title .thin{font-weight:200}
  .section-title .heavy{font-weight:900}

  .ring-label{position:absolute;font-family:"Montserrat",sans-serif;font-weight:700;font-size:15px;line-height:18px;white-space:nowrap}
  .ring-label .val{display:block;font-family:"Open Sans",sans-serif;font-weight:400;font-size:12px;color:var(--red);line-height:16px}
  .ring-label--left{text-align:right}

  .row-label{position:absolute;right:690px;font-family:"Montserrat",sans-serif;font-weight:700;font-size:16px;text-align:right}
  .bar{position:absolute;left:524px;width:353px;height:52px;display:flex;border-radius:0 26px 26px 0;overflow:hidden}
  .bar__g4{width:194px;background:var(--bar-dark);color:var(--white);display:flex;align-items:center;justify-content:center;text-align:center;font-size:16px;line-height:15px;padding-left:40px}
  .bar__g5{flex:1;background:var(--red);color:var(--white);display:flex;align-items:center;justify-content:center;text-align:center;font-size:16px;line-height:15px}
  .bar small{font-size:12px;line-height:15px}
  .col-head{position:absolute;font-family:"Montserrat",sans-serif;font-weight:700;font-size:26px}

  .gen-head{position:absolute;font-family:"Montserrat",sans-serif;font-weight:700;font-size:64px;line-height:64px}

  .landscape-title{position:absolute;left:0;width:1200px;text-align:center;font-family:"Montserrat",sans-serif;font-weight:200;font-size:42px}
  .landscape-title b{font-weight:300}
  .landscape-sub{position:absolute;left:0;width:1200px;text-align:center;font-family:"Montserrat",sans-serif;font-weight:300;font-size:24px;color:var(--red-soft)}

  .gain{position:absolute;width:446px;height:100px}
  .gain__badge{position:absolute;top:0;width:96px;height:96px;background:var(--red);color:var(--white);font-family:"Montserrat",sans-serif;font-weight:700;font-size:30px;display:flex;align-items:center;justify-content:center}
  .gain__head{position:absolute;top:0;height:32px;background:var(--ink);color:var(--white);font-family:"Montserrat",sans-serif;font-weight:300;font-size:17px;line-height:32px;padding:0 10px;white-space:nowrap}
  .gain__body{position:absolute;top:32px;width:226px;height:64px;background:var(--panel);font-size:15px;line-height:19px;display:flex;align-items:center;padding:0 10px}
  .gain__icon{position:absolute;z-index:2;top:-14px;width:124px;height:124px;border-radius:50%;background:var(--white);border:12px solid var(--ink);display:flex;align-items:center;justify-content:center}
  .gain--left .gain__badge{left:0;border-radius:48px 0 0 48px}
  .gain--left .gain__head{left:96px;width:260px}
  .gain--left .gain__body{left:96px}
  .gain--left .gain__icon{left:322px}
  .gain--right .gain__badge{right:0;border-radius:0 48px 48px 0}
  .gain--right .gain__head{right:96px;width:240px;text-align:right}
  .gain--right .gain__body{right:96px}
  .gain--right .gain__icon{left:0}
</style>
</head>
<body>

<!-- Network comparison scenes -->
<div class="art art--city" style="left:110px;top:225px;width:465px;height:350px" role="img" aria-label="Isometric city block served by a single 4G antenna tower covering terminals with a wide grey cone"></div>
<div class="art art--beam" style="left:615px;top:225px;width:465px;height:350px" role="img" aria-label="Isometric city block with a 5G massive antenna array on a tower sending narrow red beams to individual terminals"></div>
<div class="pill pill--dark" style="left:275px;top:97px;width:126px;height:74px">Current<br>(4G)</div>
<div class="pill pill--red" style="left:782px;top:97px;width:126px;height:74px">New<br>(5G)</div>
<div class="callout" style="left:147px;top:200px;width:128px;height:36px">Antenna for 4th generation<br>base stations</div>
<div class="callout" style="left:638px;top:193px;width:137px;height:40px">Massive APAA for<br>5th-generation base station</div>

<div class="rule" style="left:138px;top:607px;width:954px"></div>

<!-- Comparing ring -->
<h2 class="section-title" style="top:628px"><span class="thin">COMPARING </span><span class="heavy">4G and 5G</span></h2>

<svg class="abs" style="left:0;top:0" width="1200" height="1076" viewBox="0 0 1200 1076">
  <defs>
    <radialGradient id="hub" cx="50%" cy="45%" r="55%">
      <stop offset="0" stop-color="#ffffff"/><stop offset="1" stop-color="#d4d4d4"/>
    </radialGradient>
  </defs>
  <circle cx="639" cy="858" r="112" fill="url(#hub)" stroke="var(--ink)" stroke-width="10"/>
  <g fill="none" stroke="var(--ink)" stroke-width="3" stroke-linecap="round">
    <circle cx="639" cy="796" r="4" fill="var(--ink)"/>
    <path d="M627 786a17 17 0 0 0 0 20M651 786a17 17 0 0 1 0 20M620 779a27 27 0 0 0 0 34M658 779a27 27 0 0 1 0 34"/>
    <path d="M639 802L624 862M639 802L654 862M630 830h18M627 846h24M631 830l17 16M648 830l-17 16"/>
  </g>
  <text x="572" y="906" font-family="Montserrat,sans-serif" font-weight="600" font-size="28" fill="var(--ink)">4G</text>
  <path d="M636 896h18M648 890l7 6-7 6" fill="none" stroke="#8a8a8a" stroke-width="3"/>
  <text x="662" y="906" font-family="Montserrat,sans-serif" font-weight="600" font-size="28" fill="var(--red)">5G</text>

  <g fill="var(--white)" stroke="var(--ink)" stroke-width="6">
    <circle cx="601" cy="750" r="22"/><circle cx="541" cy="799" r="22"/><circle cx="525" cy="867" r="22"/><circle cx="551" cy="929" r="22"/><circle cx="605" cy="968" r="22"/>
  </g>
  <g fill="none" stroke="var(--red)" stroke-width="1.5">
    <circle cx="677" cy="750" r="29"/><circle cx="736" cy="799" r="29"/><circle cx="752" cy="867" r="29"/><circle cx="727" cy="929" r="29"/><circle cx="674" cy="968" r="29"/>
  </g>
  <g fill="var(--white)" stroke="var(--red)" stroke-width="6">
    <circle cx="677" cy="750" r="22"/><circle cx="736" cy="799" r="22"/><circle cx="752" cy="867" r="22"/><circle cx="727" cy="929" r="22"/><circle cx="674" cy="968" r="22"/>
  </g>
  <g fill="none" stroke="var(--ink)" stroke-width="2">
    <path d="M594 740h14M594 760h14M596 740l10 20M606 740l-10 20"/>
    <path d="M670 740h14M670 760h14M672 740l10 20M682 740l-10 20"/>
    <rect x="535" y="789" width="11" height="18" rx="2"/><rect x="730" y="789" width="11" height="18" rx="2"/>
    <path d="M525 857l-8 9h5v10h6v-10h5z"/><path d="M752 857l-8 9h5v10h6v-10h5z"/>
    <path d="M541 937v-16M541 937h20M543 933l5-7 4 4 5-8 4 11"/><path d="M717 937v-16M717 937h20M719 933l5-7 4 4 5-8 4 11"/>
    <circle cx="605" cy="968" r="9"/><path d="M596 968h18M605 959v18"/>
    <circle cx="674" cy="968" r="9"/><path d="M665 968h18M674 959v18"/>
  </g>
  <g stroke="var(--ink)" stroke-width="1.2" fill="none">
    <path d="M589 720l-8-20"/><path d="M517 785l-16-10"/><path d="M497 869h-18"/><path d="M527 952l-14 9"/><path d="M600 995l-5 20"/>
  </g>
  <g stroke="var(--red)" stroke-width="1.2" fill="none">
    <path d="M689 720l8-20"/><path d="M764 785l16-10"/><path d="M785 869h18"/><path d="M752 952l14 9"/><path d="M681 1000l4 20"/>
  </g>
</svg>

<div class="ring-label ring-label--left" style="right:640px;top:688px">LATENCY<span class="val">10 ms</span></div>
<div class="ring-label ring-label--left" style="right:715px;top:751px">DATA TRAFFIC<span class="val">7.2 Exabytes/Month</span></div>
<div class="ring-label ring-label--left" style="right:735px;top:843px">PEAK DATA RATES<span class="val">1 GB/s</span></div>
<div class="ring-label ring-label--left" style="right:712px;top:937px">AVAILABLE SPECTRUM<span class="val">3 GHz</span></div>
<div class="ring-label ring-label--left" style="right:662px;top:1007px">CONNECTION DENSITY<span class="val">100 Thousand Connections/Km²</span></div>
<div class="ring-label" style="left:710px;top:690px">LATENCY<span class="val">&lt;1 ms</span></div>
<div class="ring-label" style="left:788px;top:752px">DATA TRAFFIC<span class="val">50 Exabytes/Month (2021)</span></div>
<div class="ring-label" style="left:816px;top:843px">PEAK DATA RATES<span class="val">20 GB/s</span></div>
<div class="ring-label" style="left:780px;top:938px">AVAILABLE SPECTRUM<span class="val">30 GHz</span></div>
<div class="ring-label" style="left:704px;top:1005px">CONNECTION DENSITY<span class="val">1 Million Connections/Km²</span></div>

<div class="rule" style="left:124px;top:1076px;width:954px"></div>

<!-- Comparing table -->
<h2 class="section-title" style="top:1082px"><span class="thin">COMPARING </span><span class="heavy">4G and 5G</span></h2>
<div class="col-head" style="left:626px;top:1138px">4G</div>
<div class="col-head" style="left:772px;top:1138px;color:var(--red)">5G</div>

<div class="row-label" style="top:1194px">LATENCY</div>
<div class="bar" style="top:1179px"><div class="bar__g4">10 ms</div><div class="bar__g5">&lt;1 ms</div></div>
<div class="row-label" style="top:1263px">DATA TRAFFIC</div>
<div class="bar" style="top:1248px"><div class="bar__g4"><small>7.2<br>Exabytes/Month</small></div><div class="bar__g5"><small>50<br>Exabytes/Month (2021)</small></div></div>
<div class="row-label" style="top:1332px">PEAK DATA RATES</div>
<div class="bar" style="top:1317px"><div class="bar__g4">1GB/s</div><div class="bar__g5">20 GB/s</div></div>
<div class="row-label" style="top:1404px">AVAILABLE SPECTRUM</div>
<div class="bar" style="top:1389px"><div class="bar__g4">3 GHz</div><div class="bar__g5">30 GHz</div></div>
<div class="row-label" style="top:1472px">CONNECTION DENSITY</div>
<div class="bar" style="top:1457px"><div class="bar__g4"><small>100 Thousand<br>Connections/Km2</small></div><div class="bar__g5"><small>1Million<br>Connections/Km2</small></div></div>

<svg class="abs" style="left:518px;top:1172px" width="74" height="350" viewBox="0 0 74 350">
  <g fill="var(--red)" stroke="var(--ink)" stroke-width="6">
    <circle cx="36" cy="33" r="29"/><circle cx="36" cy="102" r="29"/><circle cx="36" cy="171" r="29"/><circle cx="36" cy="243" r="29"/><circle cx="36" cy="311" r="29"/>
  </g>
  <g fill="none" stroke="var(--ink)" stroke-width="2">
    <path d="M29 22h14M29 44h14M31 22l10 22M41 22l-10 22"/>
    <rect x="30" y="91" width="12" height="20" rx="2"/>
    <path d="M36 159l-9 10h6v12h6v-12h6z"/>
    <path d="M24 252v-18M24 252h24M26 248l6-9 5 5 5-9 5 13"/>
    <circle cx="36" cy="311" r="11"/><path d="M25 311h22M36 300v22"/>
  </g>
</svg>

<div class="rule" style="left:114px;top:1545px;width:954px"></div>

<!-- Coverage contrast -->
<div class="gen-head" style="left:342px;top:1562px">4G</div>
<div class="gen-head" style="left:852px;top:1562px;color:var(--red)">5G</div>
<svg class="abs" style="left:418px;top:1558px" width="40" height="36" viewBox="0 0 40 36"><g fill="none" stroke="var(--ink)" stroke-width="4"><path d="M4 22a10 10 0 0 1 10 10M4 12a20 20 0 0 1 20 20M4 2a30 30 0 0 1 30 30"/></g></svg>
<svg class="abs" style="left:928px;top:1558px" width="40" height="36" viewBox="0 0 40 36"><g fill="none" stroke="var(--red)" stroke-width="4"><path d="M4 22a10 10 0 0 1 10 10M4 12a20 20 0 0 1 20 20M4 2a30 30 0 0 1 30 30"/></g></svg>
<div class="art art--cone" style="left:90px;top:1635px;width:520px;height:550px" role="img" aria-label="Single 4G billboard antenna spreading one wide grey cone over a group of business people"></div>
<div class="art art--beams" style="left:690px;top:1635px;width:380px;height:550px" role="img" aria-label="5G billboard antenna grid sending separate red beams to each business person"></div>

<div class="rule" style="left:106px;top:2230px;width:954px"></div>

<!-- Landscape of 5G -->
<h2 class="landscape-title" style="top:2258px">The Landscape Of <b>5G</b></h2>
<p class="landscape-sub" style="top:2311px">5G will differentiate itself delivering various improvements</p>

<div class="gain gain--left" style="left:141px;top:2403px">
  <div class="gain__badge">10x</div>
  <div class="gain__head">Decrease in latency</div>
  <div class="gain__body">Delivering latency as 1 ms</div>
  <div class="gain__icon"><svg width="60" height="60" viewBox="0 0 60 60"><g fill="none" stroke="var(--ink)" stroke-width="3"><circle cx="34" cy="33" r="18"/><path d="M34 33V22M34 33l8 5M30 11h8M34 11v4M4 28h10M8 35h8M4 42h12"/></g></svg></div>
</div>
<div class="gain gain--right" style="left:617px;top:2403px">
  <div class="gain__icon"><svg width="60" height="60" viewBox="0 0 60 60"><g fill="none" stroke="var(--ink)" stroke-width="3"><circle cx="30" cy="16" r="3"/><path d="M22 9a11 11 0 0 0 0 14M38 9a11 11 0 0 1 0 14M30 19L20 54M30 19l10 35M24 38h12M22 46h16"/></g></svg></div>
  <div class="gain__head">Spectrum efficiency</div>
  <div class="gain__body">Achieving even more bits per Hz with advanced antenna techniques</div>
  <div class="gain__badge">3x</div>
</div>

<div class="gain gain--left" style="left:141px;top:2602px">
  <div class="gain__badge">10x</div>
  <div class="gain__head">Connection density</div>
  <div class="gain__body">Enabling more efficient signaling for IoT connectivity</div>
  <div class="gain__icon"><svg width="60" height="60" viewBox="0 0 60 60"><g fill="none" stroke="var(--ink)" stroke-width="3"><circle cx="12" cy="48" r="4"/><path d="M10 34a14 14 0 0 1 14 14M10 24a24 24 0 0 1 24 24M10 14a34 34 0 0 1 34 34M10 4a44 44 0 0 1 44 44"/></g></svg></div>
</div>
<div class="gain gain--right" style="left:617px;top:2602px">
  <div class="gain__icon"><svg width="70" height="50" viewBox="0 0 70 50"><g fill="none" stroke="var(--ink)" stroke-width="2.5"><path d="M12 12L6 46M12 12l6 34M35 12l-6 34M35 12l6 34M58 12l-6 34M58 12l6 34M7 6a7 7 0 0 0 0 10M17 6a7 7 0 0 1 0 10M30 6a7 7 0 0 0 0 10M40 6a7 7 0 0 1 0 10M53 6a7 7 0 0 0 0 10M63 6a7 7 0 0 1 0 10"/></g></svg></div>
  <div class="gain__head">Traffic capacity</div>
  <div class="gain__body">Driving network hyper-densification with more small cells everywhere</div>
  <div class="gain__badge">100x</div>
</div>

<div class="gain gain--left" style="left:141px;top:2801px">
  <div class="gain__badge">10x</div>
  <div class="gain__head">Experienced throughput</div>
  <div class="gain__body">Bringing more uniform, multi-Gbps peak rates</div>
  <div class="gain__icon"><svg width="60" height="60" viewBox="0 0 60 60"><g fill="none" stroke="var(--ink)" stroke-width="3"><path d="M6 42a24 24 0 0 1 48 0zM30 42l10-16M12 34l4 1M48 34l-4 1M30 20v4"/></g></svg></div>
</div>
<div class="gain gain--right" style="left:617px;top:2801px">
  <div class="gain__icon"><svg width="60" height="60" viewBox="0 0 60 60"><g fill="none" stroke="var(--ink)" stroke-width="3"><rect x="6" y="8" width="16" height="10"/><rect x="38" y="8" width="16" height="10"/><rect x="6" y="40" width="16" height="10"/><rect x="38" y="40" width="16" height="10"/><path d="M22 13h16M22 45h16M14 18v22M46 18v22"/></g></svg></div>
  <div class="gain__head">Network efficiency</div>
  <div class="gain__body">Optimizing network energy consumption with more efficient processing</div>
  <div class="gain__badge">100x</div>
</div>

</body>
</html>
```